Law Firm Marketing Post Card to Real Estate Agents

We need a postcard that will be used to market to real estate agents. Something clean, professional and appealing. We're marketing for a specific field (taxes) and are planning on passing out the cards to individual agents and we do not plan on mailing them. We'd like something on the front cover that truly catches someones attention and makes them want to read the back side. Text will read:

Front and Back; front will have very little text. Only the following:
Tax & Legal Strategies for Real Estate Agents
Presented by Birchwell Legal Partners, LLC
5 Tax Strategies Every Real Estate Agent Should Know

BACK COVER:
Most real estate agents are considered 1099 independent contractors, and have never been told that there are money saving strategies that could make a huge difference for them come tax time with just a few easy steps.

With our free consultation, Birchwell has one mission – to teach real estate agents 5 legal and tax planning strategies that could literally save them thousands of dollars.

Please contact us to schedule a one-on-one consultation, or an office presentation, and learn about some of the tax and legal strategies that have helped countless real estate agents and independent contractors:

- Minimize self employment tax
- Deduct 100% of out of pocket medical expenses
- Create wealth
- Deduct 100% of health insurance premiums
- Invest in real estate
- Deduct a portion of a child’s tuition and expenses
- Reduce overall tax liability

For more information, please email our office at: Info@BirchwellLegal.Example.

Target Market(s)

Real Estate Agents

Industry/Entity Type

Real Estate

Requirements
Must have
• Text listed on the front of the card as shown on the attachment.
• Clean, appealing, professional cover.
• must be similar to colors used on our website so that the reader feels like it is from the same company; please include website address on card as well - www.birchwelllegal.example

```html
<!DOCTYPE html>
<html lang="en">
<head>
<meta charset="UTF-8">
<title>Birchwell Legal Partners – Postcard Back</title>
<link href="https://fonts.googleapis.com/css2?family=Comfortaa:wght@400;600;700&display=swap" rel="stylesheet">
<style>
  :root {
    --stage: #e4e5e8;
    --card: #eef0f4;
    --card-tint: #dfe3ea;
    --ink: #2a2d36;
    --accent: #4b7fb6;
    --bullet: #3a4560;
    --stripe: #5e8dbd;
    --navy: #16203a;
    --white: #ffffff;
  }
  * { box-sizing: border-box; margin: 0; padding: 0; }
  html, body {
    width: 1200px;
    height: 1000px;
    overflow: hidden;
    background: var(--stage);
    font-family: "Comfortaa", sans-serif;
  }
  .postcard {
    position: absolute;
    left: 100px;
    top: 150px;
    width: 1000px;
    height: 700px;
    background: var(--card);
    overflow: hidden;
    box-shadow: 0 12px 40px rgba(0,0,0,0.18);
  }
  .skyline {
    position: absolute;
    right: 0;
    top: 0;
    width: 620px;
    height: 590px;
    background: linear-gradient(180deg, rgba(223,227,234,0) 0%, var(--card-tint) 55%, #d6dbe4 100%);
  }
  .body-copy {
    position: absolute;
    left: 125px;
    top: 48px;
    width: 790px;
    color: var(--ink);
    font-size: 20px;
    line-height: 25px;
    font-weight: 600;
  }
  .body-copy p { margin-bottom: 24px; }
  .strategy-list {
    list-style: none;
    margin-top: 2px;
  }
  .strategy-list li {
    display: flex;
    align-items: center;
    color: var(--accent);
    font-size: 20px;
    line-height: 29px;
    font-weight: 600;
  }
  .strategy-list svg {
    width: 14px;
    height: 14px;
    margin-right: 38px;
    flex: none;
  }
  .footer-stripe {
    position: absolute;
    left: 0;
    bottom: 100px;
    width: 100%;
    height: 12px;
    background: var(--stripe);
  }
  .footer-band {
    position: absolute;
    left: 0;
    bottom: 0;
    width: 100%;
    height: 100px;
    background: var(--navy);
    color: var(--white);
    font-size: 20px;
    font-weight: 600;
    padding: 44px 0 0 125px;
  }
  .footer-band strong { font-weight: 700; }
</style>
</head>
<body>
  <article class="postcard">
    <div class="skyline" role="img" aria-label="Faint city skyline photograph fading into the card background"></div>

    <div class="body-copy">
      <p>Most real estate agents are considered 1099 independent contractors, and have never been told that there are money saving strategies that could make a huge difference for them come tax time with just a few easy steps.</p>
      <p>With our free consultation, Birchwell has one mission – to teach real estate agents 5 legal and tax planning strategies that could literally save them thousands of dollars.</p>
      <p>Please contact us to schedule a one-on-one consultation, or an office presentation, and learn about some of the tax and legal strategies that have helped countless real estate agents and independent contractors:</p>

      <ul class="strategy-list">
        <li><svg viewBox="0 0 14 14"><path d="M3 2 L11 7 L3 12 L5 7 Z" fill="var(--bullet)"/></svg>Minimize self employment tax</li>
        <li><svg viewBox="0 0 14 14"><path d="M3 2 L11 7 L3 12 L5 7 Z" fill="var(--bullet)"/></svg>Deduct 100% of out of pocket medical expenses</li>
        <li><svg viewBox="0 0 14 14"><path d="M3 2 L11 7 L3 12 L5 7 Z" fill="var(--bullet)"/></svg>Create wealth</li>
        <li><svg viewBox="0 0 14 14"><path d="M3 2 L11 7 L3 12 L5 7 Z" fill="var(--bullet)"/></svg>Deduct 100% of health insurance</li>
        <li><svg viewBox="0 0 14 14"><path d="M3 2 L11 7 L3 12 L5 7 Z" fill="var(--bullet)"/></svg>Invest in real estate</li>
        <li><svg viewBox="0 0 14 14"><path d="M3 2 L11 7 L3 12 L5 7 Z" fill="var(--bullet)"/></svg>Deduct a portion of a child’s tuition and expenses</li>
        <li><svg viewBox="0 0 14 14"><path d="M3 2 L11 7 L3 12 L5 7 Z" fill="var(--bullet)"/></svg>Reduce overall tax liability</li>
      </ul>
    </div>

    <div class="footer-stripe"></div>
    <footer class="footer-band">For more information, please email our office at: <strong>Info@BirchwellLegal.Example.</strong></footer>
  </article>
</body>
</html>
```